realtor require a flyer to market a unit in prime district singapore

This flyer for the sale of "The Valmorelle" is to be distributed to high class district in PRIME homes in singapore. It has to be elegant but eye catching. It must also contain the following detail

1) 1605sqft
2) $2.4 mil with room for negotiation
3) Owner migrating
4) 3 + utility room
5) Desmond Kuah
6) 83527406
7) CEA no. 4718293B

In Singapore the marketing law is pretty strict hence, the following information must also be shown but may be in fine line

1) OKU Homefield network Pte Ltd with LOGO
2) Estate Agency License L5817406M

Target Market(s)

High network owners who has only that 1 sec to to catch their attention

Industry/Entity Type

Marketing

Font styles to use
Serif

Requirements
Must have
• What is stated above
Nice to have
• Nice to have the works and layout nicely crafted out

```html
<!DOCTYPE html>
<html lang="en">
<head>
<meta charset="utf-8">
<title>The Valmorelle – Property Flyer</title>
<link rel="stylesheet" href="https://fonts.googleapis.com/css2?family=Kaushan+Script&family=PT+Sans+Narrow:wght@400;700&family=PT+Sans:ital,wght@0,400;0,700;1,700&display=swap">
<style>
  :root {
    --navy: #2f2d70;
    --navy-light: #4a4790;
    --red: #c9343e;
    --red-dark: #a8252f;
    --ink: #2b2b2b;
    --rule: #a9a9a9;
    --paper: #ffffff;
    --backdrop: #e9e7e4;
  }
  * { box-sizing: border-box; margin: 0; padding: 0; }
  html, body { width: 1034px; height: 1200px; overflow: hidden; background: var(--backdrop); }
  .flyer {
    position: absolute; left: 77px; top: 30px;
    width: 880px; height: 1140px;
    background: var(--paper); overflow: hidden;
    box-shadow: 0 2px 8px rgba(0,0,0,.18);
    font-family: "PT Sans", sans-serif; color: var(--ink);
  }
  .photo-column { position: absolute; left: 440px; top: 0; width: 440px; height: 1140px; }
  .photo { position: absolute; left: 0; width: 440px; }
  .photo--terrace { top: 0; height: 258px; background: linear-gradient(160deg, #4d5a3c, #8b7a5c 60%, #c8b08a); }
  .photo--living { top: 261px; height: 284px; background: linear-gradient(170deg, #e9e3da, #c9b6a2 55%, #7a4a30); }
  .photo--bedroom { top: 548px; height: 286px; background: linear-gradient(165deg, #e6e2dc, #c7a27a 50%, #d9d6d4); }
  .photo--dining { top: 837px; height: 303px; background: linear-gradient(170deg, #ece8e1, #b99a7a 55%, #6a4a34); }
  .curve { position: absolute; left: 0; top: 0; width: 880px; height: 1140px; }

  .title { position: absolute; left: 26px; top: 38px; font-family: "Kaushan Script", cursive; font-size: 68px; color: var(--red); font-weight: 400; letter-spacing: 1px; }
  .headline { position: absolute; left: 33px; top: 158px; font-family: "PT Sans Narrow", sans-serif; font-weight: 700; font-size: 39px; line-height: 42px; color: var(--navy); }
  .rule { position: absolute; left: 33px; width: 455px; height: 2px; background: var(--rule); }
  .rule--top { top: 250px; }
  .rule--bottom { top: 298px; }
  .tagline { position: absolute; left: 37px; top: 259px; font-family: "PT Sans Narrow", sans-serif; font-size: 24px; }
  .tagline strong { font-weight: 700; }

  .thumbs { position: absolute; left: 33px; top: 318px; display: grid; grid-template-columns: 89px 89px; gap: 4px; }
  .thumb { width: 89px; height: 86px; }
  .thumb--living { background: linear-gradient(160deg, #ede8e0, #a88066); }
  .thumb--bedroom { background: linear-gradient(160deg, #e8e4de, #c79a6a); }
  .thumb--dining { background: linear-gradient(160deg, #efebe4, #8a6a50); }
  .thumb--terrace { background: linear-gradient(160deg, #5a6544, #c2ab86); }

  .features { position: absolute; left: 255px; top: 316px; list-style: none; font-family: "PT Sans Narrow", sans-serif; font-weight: 700; color: var(--red); font-size: 30px; line-height: 27px; }
  .features li { position: relative; padding-left: 55px; margin-bottom: 24px; }
  .features li.two-line { margin-bottom: 22px; }
  .features svg { position: absolute; left: 0; top: 2px; width: 36px; height: 32px; }

  .band-rule { position: absolute; left: 0; top: 547px; width: 630px; height: 4px; background: var(--navy); }
  .band-satisfaction { position: absolute; left: 0; top: 553px; width: 628px; height: 54px; background: linear-gradient(180deg, #d5434c, var(--red-dark)); color: #fff; font-family: "PT Sans Narrow", sans-serif; font-style: italic; font-weight: 700; font-size: 36px; line-height: 54px; text-align: center; padding-left: 10px; }
  .band-services { position: absolute; left: 0; top: 607px; width: 624px; height: 128px; background: radial-gradient(ellipse at 55% 100%, var(--navy-light), var(--navy) 70%); color: #fff; text-align: center; }
  .services-list { font-family: "PT Sans Narrow", sans-serif; font-weight: 700; font-size: 31px; padding-top: 20px; letter-spacing: .5px; }
  .services-list .dot { display: inline-block; width: 10px; height: 10px; border-radius: 50%; background: #fff; margin: 0 16px 6px; }
  .services-note { font-family: "PT Sans Narrow", sans-serif; font-size: 20px; line-height: 23px; margin-top: 6px; }

  .values { position: absolute; left: 60px; top: 768px; font-family: "PT Sans Narrow", sans-serif; font-size: 21px; }
  .values em { font-weight: 700; }
  .commitments { position: absolute; left: 80px; top: 808px; width: 500px; list-style: none; font-family: "PT Sans Narrow", sans-serif; font-size: 17px; line-height: 22px; }
  .commitments li { position: relative; padding-left: 30px; margin-bottom: 14px; }
  .commitments li::before { content: ""; position: absolute; left: 0; top: 10px; width: 10px; height: 10px; border-radius: 50%; background: #222; }

  .agent-portrait { position: absolute; left: 10px; top: 945px; width: 145px; height: 175px; background: linear-gradient(180deg, #f4f1ee, #d9cfc6 55%, #1f1f24); }
  .agent-name { position: absolute; left: 168px; top: 955px; font-family: "PT Sans Narrow", sans-serif; font-weight: 700; font-size: 32px; color: var(--red); }
  .agent-reg { position: absolute; left: 168px; top: 992px; font-family: "PT Sans Narrow", sans-serif; font-weight: 700; font-size: 19px; }
  .agent-rule { position: absolute; left: 168px; top: 1020px; width: 342px; height: 2px; background: var(--rule); }
  .agent-call { position: absolute; left: 168px; top: 1030px; font-family: "PT Sans Narrow", sans-serif; font-size: 19px; }
  .agent-call strong { font-size: 27px; color: var(--navy); }
  .agency { position: absolute; left: 168px; top: 1070px; display: flex; align-items: center; gap: 10px; }
  .agency-mark { width: 34px; height: 34px; background: var(--red); }
  .agency-name { font-family: "PT Sans Narrow", sans-serif; font-size: 21px; line-height: 20px; color: var(--red); }
  .agency-license { font-family: "PT Sans Narrow", sans-serif; font-size: 17px; color: var(--red); }
</style>
</head>
<body>
<main class="flyer">
  <div class="photo-column">
    <div class="photo photo--terrace" role="img" aria-label="Photo of the covered terrace with dining table and chairs"></div>
    <div class="photo photo--living" role="img" aria-label="Photo of the living room with leather sofas and ceiling fan"></div>
    <div class="photo photo--bedroom" role="img" aria-label="Photo of the master bedroom with built-in wardrobe"></div>
    <div class="photo photo--dining" role="img" aria-label="Photo of the dining area with round glass table"></div>
  </div>

  <svg class="curve" viewBox="0 0 880 1140" aria-hidden="true">
    <path d="M478,0 Q762,570 570,1140 L0,1140 L0,0 Z" fill="#2f2d70"/>
    <path d="M464,0 Q748,570 556,1140 L0,1140 L0,0 Z" fill="#c9343e"/>
    <path d="M455,0 Q739,570 547,1140 L0,1140 L0,0 Z" fill="#ffffff"/>
  </svg>

  <h1 class="title">The Valmorelle</h1>
  <h2 class="headline">MOVING ON TO YOUR NEXT<br>IDEAL PROPERTY?</h2>
  <div class="rule rule--top"></div>
  <p class="tagline"><strong>LET US</strong> walk you &amp; your family through a smooth journey!</p>
  <div class="rule rule--bottom"></div>

  <div class="thumbs">
    <div class="thumb thumb--living" role="img" aria-label="Thumbnail of the living room"></div>
    <div class="thumb thumb--bedroom" role="img" aria-label="Thumbnail of the bedroom"></div>
    <div class="thumb thumb--dining" role="img" aria-label="Thumbnail of the dining area"></div>
    <div class="thumb thumb--terrace" role="img" aria-label="Thumbnail of the terrace"></div>
  </div>

  <ul class="features">
    <li><svg viewBox="0 0 36 32"><path d="M2,17 L8,12 L14,20 L31,2 L35,6 L14,30 Z" fill="#1e1e1e"/></svg>1605sqft</li>
    <li><svg viewBox="0 0 36 32"><path d="M2,17 L8,12 L14,20 L31,2 L35,6 L14,30 Z" fill="#1e1e1e"/></svg>3 + utility room</li>
    <li class="two-line"><svg viewBox="0 0 36 32"><path d="M2,17 L8,12 L14,20 L31,2 L35,6 L14,30 Z" fill="#1e1e1e"/></svg>$2.4 mil with room<br>for negotiation</li>
    <li><svg viewBox="0 0 36 32"><path d="M2,17 L8,12 L14,20 L31,2 L35,6 L14,30 Z" fill="#1e1e1e"/></svg>Owner migrating</li>
  </ul>

  <div class="band-rule"></div>
  <div class="band-satisfaction">Your Satisfaction Is Our Goal!</div>
  <section class="band-services">
    <p class="services-list">SELL<span class="dot"></span>BUY<span class="dot"></span>RENT</p>
    <p class="services-note">We provide solutions that cater to your housing needs.<br>Feel free to talk to us. No obligations.</p>
  </section>

  <p class="values">We are <em>Sincere, Results Oriented and Committed to Serve</em></p>
  <ul class="commitments">
    <li>An up-to-date marketing analysis report will be supported to assist you in making the right decision for your property.</li>
    <li>An integrated marketing plan will be executed by our team of experienced and committed personnel to achieve desired resultrs within the shortest time.</li>
  </ul>

  <div class="agent-portrait" role="img" aria-label="Portrait of the agent, Desmond Kuah"></div>
  <p class="agent-name">DESMOND KUAH</p>
  <p class="agent-reg">CEA Reg No:&nbsp; 4718293B</p>
  <div class="agent-rule"></div>
  <p class="agent-call">Call <strong>8352 7406</strong> to acquire a detailed HOME REPORT</p>
  <div class="agency">
    <div class="agency-mark"></div>
    <div>
      <p class="agency-name">OKU Homefield network Pte Ltd</p>
      <p class="agency-license">Estate Agency License L5817406M</p>
    </div>
  </div>
</main>
</body>
</html>
```